POSTER FOR NEW MUSIC-THEATRE PRODUCTION - De Molenkantelaar

For our new theatre production 'Kraaienwals' we're looking for a new poster design.

All details can be found in the itinerary in attachment.
Updates

Dear designers

Thanks for some really good designs up to now.
Detailed feedback will follow from next week onwards since Im abroad for business and since I have very little internet access.

kind regards
Joris Kint

Target Market(s)

Theatres throughout Flanders (Belgium) when on tour in 2010-2011-2012. (expecting 70 performances)
Age is 14 up till 88 years old.

Requirements
Must have
• see itinerary in attachment
Nice to have
• Take a look to the poster design of our former production. We kind of liked the 'cool' look.
• Mind : use the new logo in attachment
Should not have
• too many colours.

```html
<!DOCTYPE html>
<html lang="nl">
<head>
<meta charset="utf-8">
<title>Kraaienwals — De Molenkantelaar</title>
<link rel="stylesheet" href="https://fonts.googleapis.com/css2?family=Inter:ital,wght@0,300;0,400;0,600;1,300&display=swap">
<style>
  :root {
    --red-top: #c81e28;
    --red-mid: #a3161f;
    --wine: #5a1424;
    --night: #262a38;
    --night-deep: #1f2a2c;
    --title-grey: rgba(205, 195, 195, 0.72);
    --label-grey: #b7a6aa;
    --name-white: #f4eeee;
    --panel-white: #ffffff;
    --panel-text: #8a8a8a;
    --badge-grey: #d9d9d9;
    --city-red: #e2001a;
    --ink: #2b2b2b;
  }
  * { margin: 0; padding: 0; box-sizing: border-box; }
  html, body { width: 848px; height: 1200px; overflow: hidden; background: #fff; }
  body { font-family: "Inter", Arial, sans-serif; }

  .poster {
    position: relative;
    width: 848px;
    height: 1200px;
    overflow: hidden;
  }
  .poster__wash {
    position: absolute; inset: 0;
    background:
      radial-gradient(ellipse 70% 18% at 30% 22%, rgba(230,50,55,0.35), transparent 70%),
      linear-gradient(180deg,
        var(--red-top) 0%,
        var(--red-mid) 38%,
        #8e1422 52%,
        var(--wine) 66%,
        #3a1e30 78%,
        var(--night) 90%,
        var(--night-deep) 100%);
  }

  .presenter {
    position: absolute;
    left: 664px; top: 28px;
    width: 42px; height: 430px;
    writing-mode: vertical-rl;
    transform: rotate(180deg);
    text-align: start;
    font-size: 32px;
    font-weight: 400;
    line-height: 42px;
    color: var(--title-grey);
    white-space: nowrap;
  }
  .title {
    position: absolute;
    left: 712px; top: 20px;
    width: 150px; height: 1125px;
    writing-mode: vertical-rl;
    transform: rotate(180deg);
    text-align: start;
    font-size: 158px;
    font-weight: 400;
    letter-spacing: -3px;
    line-height: 150px;
    color: var(--title-grey);
    white-space: nowrap;
    z-index: 3;
  }

  .credits {
    position: absolute;
    left: 34px; top: 620px;
    list-style: none;
  }
  .credits__item { height: 64px; }
  .credits__item--last { height: auto; }
  .credits__role {
    display: block;
    font-size: 13px;
    font-style: italic;
    font-weight: 300;
    color: var(--label-grey);
    line-height: 20px;
  }
  .credits__name {
    display: block;
    font-size: 14.5px;
    font-weight: 400;
    color: var(--name-white);
    line-height: 22px;
  }

  .partners {
    position: absolute;
    left: 14px; top: 1036px;
    width: 812px; height: 97px;
    background: var(--panel-white);
    z-index: 2;
  }
  .partners__client {
    position: absolute;
    left: 16px; top: 36px;
    display: flex; align-items: center; gap: 10px;
    font-size: 15px; font-weight: 600;
    color: var(--ink);
  }
  .partners__client-mark {
    width: 14px; height: 14px;
    background: var(--city-red);
  }
  .partners__publisher {
    position: absolute;
    left: 270px; top: 10px;
    font-size: 10px;
    color: var(--panel-text);
  }
  .partners__badge { position: absolute; top: 32px; height: 48px; }
  .partners__badge--region { left: 311px; width: 120px; background: var(--badge-grey); }
  .partners__badge--production { left: 463px; width: 64px; background: var(--badge-grey); border-radius: 50%; }
  .partners__badge--city { left: 550px; width: 46px; background: var(--city-red); }

  .support-note {
    position: absolute;
    left: 34px; top: 1154px;
    font-size: 7px;
    color: #8c8c96;
  }
</style>
</head>
<body>
  <main class="poster">
    <div class="poster__wash" role="img" aria-label="Painted wash from deep red at the top fading into dark night blue at the bottom"></div>

    <p class="presenter">de Molenkantelaar speelt</p>
    <h1 class="title">Kraaienwals</h1>

    <ul class="credits">
      <li class="credits__item"><span class="credits__role">Tekst</span><span class="credits__name">Hanne Verlinden</span></li>
      <li class="credits__item"><span class="credits__role">Regie</span><span class="credits__name">Pieter Van Damme</span></li>
      <li class="credits__item"><span class="credits__role">Animatie</span><span class="credits__name">Mr Jansen</span></li>
      <li class="credits__item"><span class="credits__role">Kostuumontwerp</span><span class="credits__name">Elke Dierckx</span></li>
      <li class="credits__item"><span class="credits__role">Lichtontwerp</span><span class="credits__name">Bram Van Hoorebeke</span></li>
      <li class="credits__item credits__item--last"><span class="credits__role">Muziek &amp; Spel</span><span class="credits__name">Jeroen Maes, Wouter Maes,<br>Frederik Maes, Tom Peeters, Joris Kint</span></li>
    </ul>

    <section class="partners" aria-label="Partners">
      <div class="partners__client"><span class="partners__client-mark"></span>De Molenkantelaar</div>
      <p class="partners__publisher">V.U. : Kintwerk Producties vzw, Joris Kint, Lindelei 17/2, 2100 Deurne (België)</p>
      <div class="partners__badge partners__badge--region" role="img" aria-label="Partner badge"></div>
      <div class="partners__badge partners__badge--production" role="img" aria-label="Partner badge"></div>
      <div class="partners__badge partners__badge--city" role="img" aria-label="Partner badge"></div>
    </section>

    <p class="support-note">Met de steun van de Regionale Overheid, stad Deurne en CC De Schakel Hove</p>
  </main>
</body>
</html>
```